St. Paddy’s Day Invitation

Invitation to text to people:
6th Annual St. Paddy’s Day Party
Where: The Kelterbrook’s
When: Saturday, March 25
Acoustic session by Taddeo Lindqvist from Mr. Pocketwatch
Fundraiser for Milo Ferreday ‘Open Harbor’ Fund

Target Market(s)

Adults only, all friends from our town, Moorestown, NJ

Colors
00AB8E
00BBA5
67D7C9
C6EFE9
E9F9F6
59FF00
82FF00
B8FF75
E3FFCB
F4FFEA

```html
<!DOCTYPE html>
<html lang="en">
<head>
<meta charset="utf-8">
<title>6th Annual St. Paddy’s Day Party</title>
<link rel="stylesheet" href="https://fonts.googleapis.com/css2?family=Barlow+Semi+Condensed:wght@300;500;600;700&display=swap">
<style>
  :root {
    --teal-deep: #03342e;
    --teal-dark: #065a4f;
    --teal: #00ab8e;
    --teal-bright: #00bba5;
    --teal-soft: #67d7c9;
    --teal-pale: #c6efe9;
    --teal-mist: #e9f9f6;
    --lime: #59ff00;
    --lime-bright: #82ff00;
    --lime-soft: #b8ff75;
    --lime-pale: #e3ffcb;
    --lime-mist: #f4ffea;
    --ink: #03342e;
    --shadow: rgba(2, 30, 26, 0.85);
  }
  * { margin: 0; padding: 0; box-sizing: border-box; }
  html, body {
    width: 848px; height: 1200px; overflow: hidden;
    background: var(--teal-deep);
  }
  .invitation {
    position: relative;
    width: 848px; height: 1200px;
    overflow: hidden;
    font-family: "Barlow Semi Condensed", "Arial Narrow", sans-serif;
    color: var(--lime-mist);
  }
  .singer-photo {
    position: absolute; inset: 0;
    background:
      radial-gradient(ellipse 300px 520px at 180px 420px, rgba(103,215,201,0.55), transparent 70%),
      radial-gradient(ellipse 220px 160px at 330px 150px, rgba(198,239,233,0.45), transparent 70%),
      radial-gradient(ellipse 420px 700px at 160px 900px, rgba(0,171,142,0.5), transparent 75%),
      linear-gradient(100deg, var(--teal) 0%, var(--teal-dark) 42%, var(--teal-deep) 100%);
  }
  .fund-mark {
    position: absolute; top: 122px; right: 42px;
    display: flex; align-items: center; gap: 12px;
    font-size: 34px; font-weight: 700; letter-spacing: 0.5px;
    text-transform: uppercase; color: var(--lime-mist);
  }
  .fund-mark__dot {
    width: 22px; height: 22px; border-radius: 50%;
    background: var(--lime-bright);
  }
  .details {
    position: absolute; right: 42px; top: 274px;
    display: flex; flex-direction: column; align-items: flex-end;
    text-align: right;
  }
  .title {
    font-size: 86px; font-weight: 600; line-height: 78px;
    text-transform: uppercase; letter-spacing: 0.5px;
    color: var(--white, #ffffff);
    text-shadow: 3px 4px 0 var(--shadow);
  }
  .when-where {
    margin-top: 70px;
    font-size: 46px; font-weight: 500; line-height: 70px;
    color: var(--teal-mist);
  }
  .act-intro {
    margin-top: 68px;
    font-size: 36px; font-weight: 600;
    color: var(--lime-soft);
  }
  .performer {
    margin-top: 14px;
    background: var(--lime-bright); color: var(--ink);
    font-size: 62px; font-weight: 600; line-height: 72px;
    text-transform: uppercase; padding: 0 14px;
  }
  .band {
    margin-top: 14px;
    font-size: 30px; font-weight: 300; color: var(--teal-pale);
  }
  .cause {
    margin-top: 8px;
    font-size: 20px; font-weight: 600; color: var(--lime-pale);
  }
</style>
</head>
<body>
<main class="invitation">
  <div class="singer-photo" role="img" aria-label="Teal-toned photo of a singer in sunglasses performing into a microphone"></div>

  <div class="fund-mark">
    <span class="fund-mark__dot"></span>
    <span>Open Harbor Fund</span>
  </div>

  <section class="details">
    <h1 class="title">6th Annual<br>St. Paddy’s<br>Day Party</h1>
    <p class="when-where">At The Kelterbrook’s<br>on Saturday, March 25</p>
    <p class="act-intro">Acoustic session by</p>
    <p class="performer">Taddeo Lindqvist</p>
    <p class="band">from Mr. Pocketwatch</p>
    <p class="cause">(Fundraiser for Milo Ferreday ‘Open Harbor’ Fund)</p>
  </section>
</main>
</body>
</html>
```